Envelope Design - Winner can do follow-up business

- Varindo.com is a Swiss-based online store selling business shirts and accessories for business men
- Please visit the webpage to make yourself familiar with the company. Although the text is in German, with Google translator you should be able to understand the main content.
- Our clients are mainly business men between 30 and 60 years old. Mostly with a high income working in the service industry (banking, insurance, lawyers, etc.). Sometimes there wives purchase the shirts for them ;-)
- The colors and the logo are given, as they are also used for the print materials (please see files in attachment)
- I am running several businesses and often need a talented web designer --> the winner gets substantial follow-up business
your task:
-for our company we need a new envelope design
-It should be simple and modern
-please use one of the logos in the followings.
-suprise me :)

```html
<!DOCTYPE html>
<html lang="en">
<head>
<meta charset="utf-8">
<title>Varindo Envelope</title>
<link rel="stylesheet" href="https://fonts.googleapis.com/css2?family=Open+Sans:wght@400;600&display=swap">
<style>
  :root {
    --backdrop: #ecebe8;
    --paper: #ffffff;
    --ink: #111111;
    --brand-yellow: #e6d86a;
    --brand-red: #ee2e24;
    --edge: #d6d6d6;
  }
  * { box-sizing: border-box; margin: 0; padding: 0; }
  html, body {
    width: 1200px;
    height: 881px;
    overflow: hidden;
    background: var(--backdrop);
    font-family: "Open Sans", Arial, sans-serif;
  }
  .envelope {
    position: absolute;
    left: 40px;
    top: 178px;
    width: 1120px;
    height: 526px;
    background: var(--paper);
    border: 1px solid var(--edge);
    box-shadow: 0 6px 18px rgba(0,0,0,0.12);
  }
  .top-band {
    position: absolute;
    left: 0;
    top: 0;
    width: 100%;
    height: 13px;
    display: flex;
  }
  .top-band__bar {
    width: 1021px;
    background: var(--ink);
  }
  .top-band__checks {
    flex: 1;
    display: flex;
    gap: 6px;
    padding-left: 6px;
  }
  .top-band__checks span {
    flex: 1;
    background: var(--brand-red);
  }
  .brand {
    position: absolute;
    left: 33px;
    top: 40px;
  }
  .brand__square {
    width: 42px;
    height: 42px;
    background: var(--brand-red);
    margin-left: 140px;
    margin-bottom: 20px;
  }
  .brand__name {
    color: var(--brand-yellow);
    font-weight: 600;
    font-size: 50px;
    line-height: 1;
    letter-spacing: 0.08em;
  }
  .contact {
    position: absolute;
    left: 33px;
    display: flex;
    align-items: center;
    gap: 12px;
    font-size: 22px;
    color: var(--ink);
  }
  .contact--address { top: 181px; }
  .contact--web { top: 480px; }
  .contact svg { width: 24px; height: 26px; flex: none; }
</style>
</head>
<body>
  <main class="envelope">
    <div class="top-band">
      <div class="top-band__bar"></div>
      <div class="top-band__checks"><span></span><span></span><span></span><span></span><span></span></div>
    </div>

    <div class="brand">
      <div class="brand__square"></div>
      <div class="brand__name">VARINDO</div>
    </div>

    <p class="contact contact--address">
      <svg viewBox="0 0 24 26" aria-hidden="true">
        <path d="M12 1C7 1 3.5 4.8 3.5 9.5 3.5 15.5 12 25 12 25s8.5-9.5 8.5-15.5C20.5 4.8 17 1 12 1z" fill="var(--brand-red)"/>
        <circle cx="12" cy="9.5" r="3.4" fill="var(--paper)"/>
      </svg>
      Street Name, City Name, State Zipcode
    </p>

    <p class="contact contact--web">
      <svg viewBox="0 0 24 24" aria-hidden="true" fill="none" stroke="var(--brand-red)" stroke-width="1.6">
        <circle cx="12" cy="12" r="10.5"/>
        <ellipse cx="12" cy="12" rx="4.6" ry="10.5"/>
        <line x1="1.5" y1="12" x2="22.5" y2="12"/>
        <path d="M3.5 6.5h17M3.5 17.5h17"/>
      </svg>
      www.varindo.com
    </p>
  </main>
</body>
</html>
```